Stationary for Corwin Lattimore | ||
Business card, letterhead, with compliments slip, envelope | ||
Use same font as used in my logo | ||
Corporate Traditional Professional Simple |
[firstname] [surname] | ||
[title] | ||
1 Some Street Sometown Somewhereshire SW23 8SW |
someone@corwinlattimore.example | ||
www.corwinlattimore.example | ||
I am the sole employee at the moment. In the future, I hope to have other employees, so I will add a 'title' section later. Please bear this in mind when positioning the information. I am looking for something that is elegant, professional, minimilistic and tasteful. Please take a look at the website: http://www.corwinlattimore.example using the following credentials to log in: u/n: "pinewhisk" p/w: "pinewhisk847" Please feel free to message me for more information. Most importantly, I want the logo and other key information (like my name?) to be in silver (PMS 877 Metallic). |
I am flexible on this. I want space on my business cards for people to be able to write some information on. | ||

```html
<!DOCTYPE html>
<html lang="en">
<head>
<meta charset="utf-8">
<title>Corwin Lattimore — Stationery</title>
<link rel="stylesheet" href="https://fonts.googleapis.com/css2?family=Cinzel:wght@400&family=Cormorant+Garamond:wght@400&display=swap">
<style>
  :root {
    --paper: #ffffff;
    --backdrop: #ffffff;
    --edge: #c9c9c9;
    --silver: #8e9092;
    --ink: #8a8a8a;
  }
  * { box-sizing: border-box; margin: 0; padding: 0; }
  html, body { width: 1200px; height: 1067px; overflow: hidden; background: var(--backdrop); }
  body { position: relative; font-family: "Cormorant Garamond", Georgia, serif; color: var(--ink); }

  .sheet { position: absolute; background: var(--paper); border: 1px solid var(--edge); }

  .wordmark { position: absolute; display: flex; align-items: center; gap: 6px; color: var(--silver); font-family: "Cinzel", Georgia, serif; font-weight: 400; line-height: 0.95; }
  .wordmark-square { background: var(--silver); flex: none; }
  .wordmark-name { display: flex; flex-direction: column; letter-spacing: 0.02em; }

  .details { position: absolute; font-size: 7px; line-height: 1.55; color: var(--ink); letter-spacing: 0.03em; }

  /* Envelope */
  .envelope { left: 57px; top: 57px; width: 621px; height: 267px; }
  .envelope .wordmark { left: 34px; top: 28px; font-size: 15px; }
  .envelope .wordmark-square { width: 14px; height: 14px; }
  .envelope .details { left: 58px; top: 64px; }

  /* Letterhead */
  .letterhead { left: 57px; top: 354px; width: 558px; height: 708px; }
  .letterhead .wordmark { left: 48px; top: 64px; font-size: 19px; }
  .letterhead .wordmark-square { width: 18px; height: 18px; }
  .letterhead .details { left: 324px; top: 66px; }

  /* Compliments slip */
  .compliments { left: 636px; top: 354px; width: 555px; height: 357px; }
  .compliments .wordmark { left: 30px; top: 26px; font-size: 19px; }
  .compliments .wordmark-square { width: 18px; height: 18px; }
  .compliments-label { position: absolute; left: 63px; top: 324px; font-family: "Cinzel", Georgia, serif; font-size: 11px; letter-spacing: 0.08em; color: var(--silver); }

  /* Business cards */
  .card { width: 231px; height: 132px; left: 636px; }
  .card-front { top: 738px; }
  .card-front .wordmark { left: 50px; top: 50px; font-size: 15px; }
  .card-front .wordmark-square { width: 14px; height: 14px; }
  .card-back { top: 882px; }
  .card-back .wordmark { left: 10px; top: 12px; font-size: 11px; gap: 4px; }
  .card-back .wordmark-square { width: 10px; height: 10px; }
  .card-back .card-web { position: absolute; left: 138px; top: 26px; font-size: 6px; color: var(--ink); }
  .card-back .card-person { position: absolute; left: 30px; top: 62px; font-size: 7px; line-height: 1.5; color: var(--silver); }
  .card-back .details { left: 30px; top: 92px; font-size: 6px; }
</style>
</head>
<body>

  <section class="sheet envelope" aria-label="Envelope">
    <div class="wordmark"><span class="wordmark-square"></span><span class="wordmark-name"><span>Corwin</span><span>Lattimore</span></span></div>
    <div class="details">
      <p>www.corwinlattimore.example</p>
      <p>&nbsp;</p>
      <p>1 Some Street</p>
      <p>Sometown</p>
      <p>Somewhereshire</p>
      <p>SW23 8SW</p>
    </div>
  </section>

  <section class="sheet letterhead" aria-label="Letterhead">
    <div class="wordmark"><span class="wordmark-square"></span><span class="wordmark-name"><span>Corwin</span><span>Lattimore</span></span></div>
    <div class="details">
      <p>e: someone@corwinlattimore.example</p>
      <p>1 Some Street, Sometown, Somewhereshire, SW23 8SW</p>
      <p>&nbsp;</p>
      <p>www.corwinlattimore.example</p>
    </div>
  </section>

  <section class="sheet compliments" aria-label="With compliments slip">
    <div class="wordmark"><span class="wordmark-square"></span><span class="wordmark-name"><span>Corwin</span><span>Lattimore</span></span></div>
    <p class="compliments-label">With Compliments</p>
  </section>

  <section class="sheet card card-front" aria-label="Business card front">
    <div class="wordmark"><span class="wordmark-square"></span><span class="wordmark-name"><span>Corwin</span><span>Lattimore</span></span></div>
  </section>

  <section class="sheet card card-back" aria-label="Business card back">
    <div class="wordmark"><span class="wordmark-square"></span><span class="wordmark-name"><span>Corwin</span><span>Lattimore</span></span></div>
    <p class="card-web">www.corwinlattimore.example</p>
    <div class="card-person">
      <p>Firstname Surname</p>
      <p>Title</p>
    </div>
    <div class="details">
      <p>e: someone@corwinlattimore.example</p>
      <p>1 Some Street, Sometown</p>
      <p>Somewhereshire, SW23 8SW</p>
    </div>
  </section>

</body>
</html>
```